Business Card for: Northbrook Financial Advisory Services Inc.

provide strategic financial advisory services to companies in the areas of corporate finance, mergers and acquisitions, executive coaching and strategic planning

Target Market(s)

Companies, banks, accountants, lawyers

Industry/Entity Type

High end business consulting in corporate finance, mergers and acquisitions, consulting

Contact Information for Business Card

Name of company, Name: xxxxxx xxxxxx , CEO, - phone number: 1-xxx-xxx-xxxx, - email address,

Requirements
Must have
• Must be professional and simple.
Nice to have
• simple, straight graphics, must give the impression that we are trustworthy, professional, competent
Should not have
• loud colors, loud design features

```html
<!DOCTYPE html>
<html lang="en">
<head>
<meta charset="utf-8">
<title>Northbrook Financial Advisory Services Inc. — Business Card</title>
<link rel="stylesheet" href="https://fonts.googleapis.com/css2?family=Poppins:wght@400;500;600;700&display=swap">
<style>
  :root {
    --brand-blue: #0b5aa6;
    --brand-navy: #0a4f98;
    --accent-sky: #1aa3e0;
    --paper: #ffffff;
    --backdrop: #e9ebee;
    --card-shadow: rgba(10, 30, 60, 0.22);
  }
  * { margin: 0; padding: 0; box-sizing: border-box; }
  html, body {
    width: 1200px; height: 880px; overflow: hidden;
    background: var(--backdrop);
    font-family: "Poppins", sans-serif;
  }
  .canvas {
    position: relative; width: 1200px; height: 880px;
  }
  .card {
    position: absolute; left: 250px; width: 700px; height: 400px;
    border-radius: 26px; overflow: hidden;
    box-shadow: 0 14px 34px var(--card-shadow);
  }
  .card-back { top: 24px; background: var(--brand-blue); }
  .card-front { top: 456px; background: var(--paper); }

  .wordmark { position: absolute; line-height: 1; }
  .wordmark-name {
    display: block; font-weight: 700; letter-spacing: -0.5px;
  }
  .wordmark-tagline {
    display: block; font-weight: 700; letter-spacing: 1.6px;
  }

  .card-back .wordmark {
    left: 0; right: 0; top: 150px; text-align: center; color: var(--paper);
  }
  .card-back .wordmark-name { font-size: 66px; }
  .card-back .wordmark-tagline { font-size: 15px; margin-top: 14px; }

  .card-front .wordmark {
    left: 70px; top: 70px; color: var(--brand-navy);
  }
  .card-front .wordmark-name { font-size: 56px; }
  .card-front .wordmark-tagline { font-size: 13px; margin-top: 10px; }

  .holder { position: absolute; left: 112px; top: 196px; }
  .holder-name {
    font-size: 28px; font-weight: 700; color: var(--brand-navy); line-height: 1.1;
  }
  .holder-role {
    font-size: 16px; font-weight: 400; color: var(--accent-sky); margin-top: 2px;
  }
  .holder-rule {
    width: 78px; height: 3px; background: var(--accent-sky); margin-top: 8px;
  }

  .contact-list {
    position: absolute; left: 112px; top: 290px; list-style: none;
  }
  .contact-item {
    display: flex; align-items: center; gap: 12px;
    font-size: 17px; color: var(--brand-navy); line-height: 1; margin-bottom: 11px;
  }
  .contact-icon { width: 22px; height: 22px; flex: none; }

  .footer-band { position: absolute; left: 0; bottom: 0; width: 700px; height: 60px; }
  .web-address {
    position: absolute; left: 380px; width: 320px; bottom: 0;
    height: 46px; line-height: 46px; text-align: center;
    font-size: 15px; font-weight: 500; color: var(--paper); letter-spacing: 0.3px;
    white-space: nowrap;
  }
</style>
</head>
<body>
<main class="canvas">

  <section class="card card-back" aria-label="Card back">
    <div class="wordmark">
      <span class="wordmark-name">Northbrook</span>
      <span class="wordmark-tagline">Financial Advisory Services Inc.</span>
    </div>
  </section>

  <section class="card card-front" aria-label="Card front">
    <div class="wordmark">
      <span class="wordmark-name">Northbrook</span>
      <span class="wordmark-tagline">Financial Advisory Services Inc.</span>
    </div>

    <div class="holder">
      <p class="holder-name">Daniel R Hale</p>
      <p class="holder-role">CEO</p>
      <div class="holder-rule"></div>
    </div>

    <ul class="contact-list">
      <li class="contact-item">
        <svg class="contact-icon" viewBox="0 0 22 22" aria-hidden="true">
          <circle cx="11" cy="11" r="11" fill="var(--accent-sky)"/>
          <path d="M7.6 6.2l1.8-.4 1 2.4-1.2 1a6.4 6.4 0 0 0 3.6 3.6l1-1.2 2.4 1-.4 1.8c-.2.5-.7.8-1.2.8A8.3 8.3 0 0 1 6.8 7.4c0-.5.3-1 .8-1.2z" fill="#fff"/>
        </svg>
        <span>1-555-210-4388</span>
      </li>
      <li class="contact-item">
        <svg class="contact-icon" viewBox="0 0 22 22" aria-hidden="true">
          <circle cx="11" cy="11" r="11" fill="var(--accent-sky)"/>
          <rect x="5.5" y="7.5" width="11" height="7.5" rx="1" fill="#fff"/>
          <path d="M5.8 8l5.2 4 5.2-4" fill="none" stroke="var(--accent-sky)" stroke-width="1.1"/>
        </svg>
        <span>info@northbrookadvisory.com</span>
      </li>
    </ul>

    <svg class="footer-band" viewBox="0 0 700 60" aria-hidden="true">
      <polygon points="0,50 0,60 700,60 700,36 370,36" fill="var(--accent-sky)"/>
      <polygon points="380,14 700,14 700,60 380,60" fill="var(--brand-navy)"/>
    </svg>
    <span class="web-address">www.northbrookadvisory.com</span>
  </section>

</main>
</body>
</html>
```